Rack card for marketing

Office to office marketing for GRM KNEE CARE

Target Market(s)

Medical Offices, Retired patients looking to maintain active lifestlye. Family practice medical offices

Industry/Entity Type

Medical

Colors
0054AA
0677BA
7BADD7
CADEEF
E8F1F8

Requirements
Must have
• Font that matches logo, GRM logo, graphic of a retiree who looks active and happy versus a knee graphic
Nice to have
• The best ever rack card!!! Easy to Read, simplicity is key.

```html
<!DOCTYPE html>
<html lang="en">
<head>
<meta charset="utf-8">
<title>GRM Knee Care – Rack Cards</title>
<link href="https://fonts.googleapis.com/css2?family=Lato:wght@400;700;900&family=Oswald:wght@500&display=swap" rel="stylesheet">
<style>
  :root{
    --bg:#7b7b7b;
    --blue:#0b66cc;
    --blue-deep:#0054aa;
    --sky:#2aa8ff;
    --sky-soft:#7badd7;
    --mist:#cadeef;
    --gray-panel:#ececee;
    --ink:#1b1d22;
    --white:#ffffff;
    --photo-a:#c9d9ee;
    --photo-b:#a9bfdc;
    --photo-c:#e6d4c8;
    --photo-dark-a:#1d2a44;
    --photo-dark-b:#b56a6a;
  }
  *{margin:0;padding:0;box-sizing:border-box}
  html,body{width:1200px;height:904px;overflow:hidden;background:var(--bg)}
  .canvas{position:relative;width:1200px;height:904px;overflow:hidden;background:var(--bg);font-family:"Lato",sans-serif;color:var(--ink)}
  .rack-card{position:absolute;top:137px;width:260px;height:630px;background:var(--white);overflow:hidden}
  .rack-card--classic{left:321px}
  .rack-card--hex{left:620px}
  .layer{position:absolute;left:0;top:0}
  .gray-panel{position:absolute;left:0;width:260px;background:var(--gray-panel)}
  .brand{position:absolute;left:18px;top:21px;width:84px;text-align:center}
  .brand-mark{width:48px;height:48px;border-radius:50%;background:var(--blue-deep);margin:0 auto 7px}
  .brand-name{font-weight:700;font-size:11px;line-height:14px;color:var(--sky);letter-spacing:.3px;white-space:nowrap}
  .tagline{position:absolute;font-family:"Oswald",sans-serif;font-weight:500;color:var(--white);font-size:15.5px;line-height:18.5px;letter-spacing:-.2px}
  .intro{position:absolute;left:19px;font-size:10.6px;line-height:13.6px;color:var(--ink)}
  .rack-card--classic .intro{width:222px;text-align:justify;text-align-last:left}
  .section-title{position:absolute;left:18px;font-weight:900;font-size:14px;color:var(--sky);letter-spacing:.2px;white-space:nowrap}
  .sub-title{position:absolute;left:18px;font-weight:900;font-size:11.6px;color:var(--blue-deep);white-space:nowrap}
  .body-copy{position:absolute;left:19px;font-size:10.6px;line-height:13.6px;color:var(--ink)}
  .rack-card--hex .body-copy{font-size:9.6px;line-height:12.4px}
  .footer-band{position:absolute;left:0;top:580px;width:260px;height:50px;background:var(--blue)}
  .contact{position:absolute;left:18px;color:var(--white);font-weight:700;font-size:10.6px;display:flex;align-items:center;gap:4px;white-space:nowrap}
  .contact .label{margin-right:2px}
  .icon{width:10px;height:10px;flex:none}
</style>
</head>
<body>
<div class="canvas">

  <!-- Card one: angled layout -->
  <section class="rack-card rack-card--classic">
    <div class="gray-panel" style="top:214px;height:134px"></div>

    <svg class="layer" width="260" height="214" viewBox="0 0 260 214">
      <defs>
        <linearGradient id="retireeTone" x1="0" y1="0" x2="1" y2="1">
          <stop offset="0" stop-color="var(--photo-a)"/>
          <stop offset=".6" stop-color="var(--photo-b)"/>
          <stop offset="1" stop-color="var(--photo-c)"/>
        </linearGradient>
      </defs>
      <polygon points="170,0 260,0 260,214" fill="var(--sky)"/>
      <polygon role="img" aria-label="Photo of an active retiree holding her knee" points="95,121 170,16 260,16 260,214 112,214 139,168" fill="url(#retireeTone)"/>
      <line x1="98" y1="118" x2="168" y2="14" stroke="var(--sky)" stroke-width="2"/>
      <polygon points="0,121 95,121 139,168 110,214 0,214" fill="var(--blue)"/>
      <polyline points="100,121 144,168 116,214" fill="none" stroke="var(--sky)" stroke-width="2"/>
    </svg>

    <div class="brand">
      <div class="brand-mark"></div>
      <div class="brand-name">GRM KNEE CARE</div>
    </div>

    <p class="tagline" style="left:18px;top:137px">For treatment<br>of knee pain for<br>medical practice</p>

    <p class="intro" style="top:224px">Knee pain is an extremely common symptom that can result from everything from a temporary injury to a chronic condition like arthritis. You can usually treat knee pain at home with rest and over-the-counter medicine. Visit a healthcare provider if you’ve experienced an injury or have knee pain for more than a few days in a row.</p>

    <h2 class="section-title" style="top:360px">CARE AND TREATMENT</h2>
    <h3 class="sub-title" style="top:379px">How is knee pain treated?</h3>
    <p class="body-copy" style="top:392px;width:145px">Which treatments you’ll need for knee pain will depend on what’s causing it. A healthcare provider will suggest treatments based on the pain’s severity &amp; its cause.</p>

    <svg class="layer" width="260" height="630" viewBox="0 0 260 630" style="pointer-events:none">
      <defs>
        <linearGradient id="kneeToneA" x1="0" y1="0" x2="1" y2="1">
          <stop offset="0" stop-color="var(--photo-dark-a)"/>
          <stop offset=".55" stop-color="var(--photo-dark-b)"/>
          <stop offset="1" stop-color="var(--photo-dark-a)"/>
        </linearGradient>
      </defs>
      <polygon points="164,396 260,371 260,463 181,485" fill="var(--sky)"/>
      <polygon role="img" aria-label="Photo of hands holding a painful knee" points="169,400 260,377 260,458 184,479" fill="url(#kneeToneA)"/>
      <polygon points="216,486 231,484 229,494" fill="var(--blue)"/>
      <polygon points="204,630 260,532 260,562 222,630" fill="var(--sky)"/>
    </svg>

    <h3 class="sub-title" style="top:497px">RICE method for knee pain</h3>
    <p class="body-copy" style="top:510px;width:222px">Which treatments you’ll need for knee pain will depend on what’s causing it. A healthcare provider will suggest treatments based on the pain’s severity and its cause.</p>

    <div class="footer-band"></div>
    <svg class="layer" width="260" height="630" viewBox="0 0 260 630">
      <polygon points="232,580 260,532 260,562 240,596 222,630 204,630" fill="var(--sky)"/>
    </svg>
    <p class="contact" style="top:587px"><span class="label">CALL US TODAY</span>
      <svg class="icon" viewBox="0 0 10 10"><circle cx="5" cy="5" r="5" fill="var(--sky)"/><path d="M3.3 2.6l1 1-.5.6a3 3 0 0 0 1.9 1.9l.6-.5 1 1-.6.8C5 7.2 2.8 5 2.6 3.2z" fill="var(--white)"/></svg>
      555-214-7390</p>
    <p class="contact" style="top:602px;font-size:10.4px">
      <svg class="icon" viewBox="0 0 10 10"><circle cx="5" cy="5" r="5" fill="var(--sky)"/><circle cx="5" cy="5" r="3" fill="none" stroke="var(--white)" stroke-width=".7"/><path d="M2 5h6M5 2v6" stroke="var(--white)" stroke-width=".7"/></svg>
      www.grmkneecare.com</p>
  </section>

  <!-- Card two: hexagon layout -->
  <section class="rack-card rack-card--hex">
    <div class="gray-panel" style="top:214px;height:172px"></div>

    <svg class="layer" width="260" height="300" viewBox="0 0 260 300">
      <defs>
        <linearGradient id="retireeToneB" x1="0" y1="0" x2="1" y2="1">
          <stop offset="0" stop-color="var(--photo-a)"/>
          <stop offset=".6" stop-color="var(--photo-b)"/>
          <stop offset="1" stop-color="var(--photo-c)"/>
        </linearGradient>
      </defs>
      <path d="M231 0H260V48L248 38C236 28 231 20 231 8Z" fill="var(--sky)"/>
      <polygon points="184,29 322,160 234,290 98,158" fill="none" stroke="var(--sky)" stroke-width="2.5" stroke-linejoin="round"/>
      <polygon role="img" aria-label="Photo of an active retiree holding her knee" points="184,37 312,160 234,282 106,158" fill="url(#retireeToneB)"/>
      <polygon points="27,121 102,121 128,185 102,249 27,249 0,185" fill="none" stroke="var(--sky)" stroke-width="2" stroke-linejoin="round"/>
      <polygon points="31,127 98,127 121,185 98,243 31,243 6,185" fill="var(--blue)" stroke="var(--blue)" stroke-width="4" stroke-linejoin="round"/>
    </svg>

    <div class="brand">
      <div class="brand-mark"></div>
      <div class="brand-name">GRM KNEE CARE</div>
    </div>

    <p class="tagline" style="left:16px;top:155px;font-size:14.5px;line-height:17.5px">For treatment<br>of knee pain for<br>medical practice</p>

    <p class="intro" style="top:266px;font-size:10.2px;line-height:13px">Knee pain is an extremely<br>common symptom that can result<br>from everything from a temporary injury to<br>a chronic condition like arthritis. You can<br>usually treat knee pain at home with rest and<br>over-the-counter medicine. Visit a healthcare<br>provider if you’ve experienced an injury or have<br>knee pain for more than a few days in a row.</p>

    <h2 class="section-title" style="top:392px">CARE AND TREATMENT</h2>
    <h3 class="sub-title" style="top:410px">How is knee pain treated?</h3>
    <p class="body-copy" style="top:425px;width:226px">Which treatments you’ll need for knee pain will depend on what’s causing it. A healthcare provider will suggest treatments based on the pain’s severity and its cause.</p>

    <h3 class="sub-title" style="top:482px">RICE method for knee pain</h3>
    <p class="body-copy" style="top:499px;width:162px">Which treatments you’ll need for knee pain will depend on what’s causing it. A healthcare provider will suggest treatments based on the pain’s severity and its cause.</p>

    <div class="footer-band"></div>
    <svg class="layer" width="260" height="630" viewBox="0 0 260 630">
      <defs>
        <linearGradient id="kneeToneB" x1="0" y1="0" x2="1" y2="1">
          <stop offset="0" stop-color="var(--photo-dark-a)"/>
          <stop offset=".55" stop-color="var(--photo-dark-b)"/>
          <stop offset="1" stop-color="var(--photo-dark-a)"/>
        </linearGradient>
      </defs>
      <polygon points="154,598 232,484 270,484 270,640 196,640" fill="none" stroke="var(--sky)" stroke-width="2.5" stroke-linejoin="round"/>
      <polygon role="img" aria-label="Photo of hands holding a painful knee" points="161,598 236,490 262,490 262,632 200,632" fill="url(#kneeToneB)"/>
    </svg>
    <p class="contact" style="top:587px">
      <svg class="icon" viewBox="0 0 10 10"><circle cx="5" cy="5" r="5" fill="var(--sky)"/><path d="M3.3 2.6l1 1-.5.6a3 3 0 0 0 1.9 1.9l.6-.5 1 1-.6.8C5 7.2 2.8 5 2.6 3.2z" fill="var(--white)"/></svg>
      555-214-7390</p>
    <p class="contact" style="top:604px;font-size:9.6px">
      <svg class="icon" viewBox="0 0 10 10"><circle cx="5" cy="5" r="5" fill="var(--sky)"/><circle cx="5" cy="5" r="3" fill="none" stroke="var(--white)" stroke-width=".7"/><path d="M2 5h6M5 2v6" stroke="var(--white)" stroke-width=".7"/></svg>
      www.grmkneecare.com</p>
  </section>

</div>
</body>
</html>
```